Poster Design Project

Simple, very easy design project.

Design for a 20" x 30" poster (I will print the poster, you do the high-res design), of the attached.

(Pls note, this JPG is sideways and is an error). You are designing PORTRAIT

```html
<!DOCTYPE html>
<html lang="en">
<head>
<meta charset="utf-8">
<title>Great Ecommerce Poster</title>
<link rel="stylesheet" href="https://fonts.googleapis.com/css2?family=Audiowide&family=Jura:wght@300;400&display=swap">
<style>
  :root {
    --paper: #ffffff;
    --tech-deep: #1a73b5;
    --tech-mid: #3f9ad6;
    --tech-light: #a9d4f0;
    --title-blue: #1467a8;
    --value-navy: #15355f;
    --rule-red: #d8322f;
  }
  html, body {
    margin: 0;
    padding: 0;
    width: 825px;
    height: 1200px;
    overflow: hidden;
    background: var(--paper);
  }
  .poster {
    position: relative;
    width: 825px;
    height: 1200px;
    background: var(--paper);
  }
  .tech-backdrop {
    position: absolute;
    left: 37px;
    top: 31px;
    width: 758px;
    height: 1140px;
    background: linear-gradient(
      to bottom,
      var(--tech-deep) 0%,
      var(--tech-mid) 10%,
      var(--tech-light) 24%,
      #eaf5fc 34%,
      var(--paper) 42%,
      var(--paper) 72%,
      #e6f3fb 78%,
      var(--tech-light) 85%,
      var(--tech-mid) 93%,
      var(--tech-deep) 100%
    );
  }
  .title {
    position: absolute;
    left: 0;
    width: 825px;
    margin: 0;
    text-align: center;
    font-family: "Audiowide", sans-serif;
    font-weight: 400;
    color: var(--title-blue);
    text-transform: uppercase;
    line-height: 1;
  }
  .title-great {
    top: 228px;
    font-size: 86px;
    letter-spacing: 2px;
  }
  .title-ecommerce {
    top: 312px;
    font-size: 86px;
    letter-spacing: 1px;
  }
  .values {
    position: absolute;
    left: 0;
    top: 0;
    width: 825px;
    height: 1200px;
    margin: 0;
    padding: 0;
    list-style: none;
  }
  .value {
    position: absolute;
    left: 0;
    width: 825px;
    text-align: center;
    font-family: "Jura", sans-serif;
    font-weight: 300;
    font-size: 60px;
    line-height: 1;
    color: var(--value-navy);
    white-space: nowrap;
  }
  .rule {
    position: absolute;
    left: 179px;
    width: 482px;
    height: 1px;
    background: var(--rule-red);
  }
</style>
</head>
<body>
  <main class="poster">
    <div class="tech-backdrop" role="img" aria-label="Blue digital technology backdrop with circuit lines, binary digits and a glowing globe, fading to white in the middle"></div>

    <h1 class="title title-great">Great</h1>
    <h1 class="title title-ecommerce">Ecommerce</h1>

    <ul class="values">
      <li class="value" style="top:435px">Diversity Of Thought</li>
      <li class="value" style="top:509px">Desire To Learn</li>
      <li class="value" style="top:583px">Never Settle</li>
      <li class="value" style="top:658px">Be A Problem Solver</li>
      <li class="value" style="top:732px">Work Fast (Web Speed)</li>
      <li class="value" style="top:804px">Execution - A Way Of Life</li>
    </ul>

    <div class="rule" style="top:502px"></div>
    <div class="rule" style="top:577px"></div>
    <div class="rule" style="top:644px"></div>
    <div class="rule" style="top:719px"></div>
    <div class="rule" style="top:797px"></div>
  </main>
</body>
</html>
```